New home full landscape package

We have a landscape construction company and have built a new home landscape package and wish to have it on a double sided a5 brochure for us to leave with sales agents. I have attached everything i can think off that would need to be incorporated and am accessible to answer any questions required.

Target Market(s)

new home buyers

Industry/Entity Type

Landscaping

Requirements
Must have
• highlighting $9990 + gst component
• clear directive/ outcome for clients
• 'whats in it for them' feel
Nice to have
• simple, elegant, clean
Should not have
• not be too busy

```html
<!DOCTYPE html>
<html lang="en">
<head>
<meta charset="utf-8">
<title>Verdant Yards – New Home Landscape Package</title>
<link rel="stylesheet" href="https://fonts.googleapis.com/css2?family=Oswald:wght@300&family=Roboto+Condensed:ital,wght@0,300;0,400;0,700;1,400&family=Cabin:wght@400;500&family=Dancing+Script:wght@500&display=swap">
<style>
:root{
  --bg:#8c8c8a;
  --orange:#e2861c;
  --green:#9cc43a;
  --green-dark:#7fae2a;
  --white:#ffffff;
  --ink:#3b3b3b;
  --sky-top:#4f6f94;
  --sky-low:#c9d3dc;
  --lawn:#6e8f3a;
}
*{box-sizing:border-box;margin:0;padding:0}
html,body{width:1200px;height:800px;overflow:hidden;background:var(--bg)}
body{position:relative;font-family:"Cabin",sans-serif}
.page{position:absolute;top:69px;width:467px;height:661px;background:var(--white);overflow:hidden;box-shadow:0 2px 6px rgba(0,0,0,.35)}
.page--front{left:111px}
.page--back{left:642px}

/* front */
.hero-photo{position:absolute;left:0;top:0;width:467px;height:305px;background:linear-gradient(180deg,var(--sky-top) 0%,var(--sky-low) 45%,#a99b8a 70%,var(--lawn) 100%)}
.guide{position:absolute;background:rgba(255,255,255,.9)}
.guide--v1{left:142px;top:0;width:2px;height:110px}
.guide--v2{left:335px;top:192px;width:2px;height:113px}
.guide--h1{left:0;top:148px;width:77px;height:2px}
.guide--h2{left:419px;top:148px;width:48px;height:2px}
.brand-box{position:absolute;left:77px;top:109px;width:342px;height:82px;background:rgba(255,255,255,.8);border-radius:4px;display:flex;align-items:center;justify-content:center;gap:12px}
.brand-mark{width:26px;height:26px;background:var(--orange)}
.brand-name{font-family:"Cabin",sans-serif;font-weight:500;font-size:34px;color:var(--orange);letter-spacing:.5px}
.offer-band{position:absolute;left:3px;top:310px;width:458px;height:102px;background:var(--orange);padding:2px 0 0 12px}
.offer-title{font-family:"Oswald",sans-serif;font-weight:300;font-size:32px;line-height:33px;color:var(--white);letter-spacing:.4px;white-space:nowrap}
.offer-from{position:absolute;left:22px;top:64px;font-family:"Dancing Script",cursive;font-size:30px;line-height:34px;color:var(--white);white-space:nowrap}
.price-tag{position:absolute;left:205px;top:381px;width:229px;height:50px;background:var(--green);color:var(--white);font-family:"Roboto Condensed",sans-serif;font-weight:700;font-size:40px;line-height:50px;text-align:center}
.benefits{position:absolute;left:33px;top:436px;list-style:none}
.benefits li{display:flex;align-items:center;height:22.4px;font-size:12.4px;color:var(--ink)}
.benefits svg{width:18px;height:16px;margin-right:6px;flex:none}
.call{position:absolute;left:274px;top:539px;font-family:"Roboto Condensed",sans-serif;font-weight:700;color:var(--orange);text-align:left}
.call-label{font-size:40px;line-height:40px;border-bottom:2px solid var(--orange);display:inline-block}
.call-number{font-size:31px;line-height:36px}
.grass{position:absolute;left:0;bottom:0;width:467px;height:46px;background:linear-gradient(180deg,rgba(156,196,58,0) 0%,var(--green) 55%,var(--green-dark) 100%)}

/* back */
.intro{position:absolute;left:14px;top:14px;width:438px;height:58px;background:var(--orange);color:var(--white);font-family:"Roboto Condensed",sans-serif;font-style:italic;font-weight:400;font-size:22px;line-height:24px;text-align:center;padding-top:5px}
.option{position:absolute;background:var(--green);color:var(--white)}
.option h3{background:var(--orange);font-family:"Cabin",sans-serif;font-weight:500;font-size:15px;height:27px;line-height:27px;padding-left:16px}
.option ul{list-style:none;padding:7px 0 0 16px}
.option li{display:flex;align-items:flex-start;font-size:12px;line-height:18.4px}
.option p{font-size:12px;line-height:16px;padding:6px 12px 0 14px}
.leaf{width:8px;height:11px;background:var(--white);border-radius:0 100% 0 100%;transform:rotate(20deg);margin:3px 9px 0 0;flex:none}
.opt-turf{left:14px;top:77px;width:217px;height:150px}
.opt-turf ul{padding-top:10px}
.opt-turf li{line-height:21.6px}
.opt-turf .leaf{margin-top:5px}
.opt-rocks{left:236px;top:77px;width:218px;height:73px}
.opt-planting{left:236px;top:154px;width:218px;height:73px}
.opt-planting ul{padding-left:14px;padding-top:5px}
.opt-planting li{line-height:16px}
.opt-planting .leaf{margin-top:2px;margin-right:4px}
.opt-other{left:14px;top:231px;width:217px;height:168px}
.opt-other ul{padding-top:3px}
.opt-edging{left:236px;top:231px;width:218px;height:210px}
.opt-edging ul{padding-left:14px}
.opt-concrete{left:14px;top:403px;width:217px;height:77px}
.opt-decking{left:236px;top:446px;width:218px;height:34px;background:var(--orange)}
.opt-decking h3{height:34px;line-height:34px}
.opt-fencing{left:14px;top:484px;width:440px;height:106px}
.opt-fencing h3{padding-left:20px}
.fence-cols{display:flex;padding:6px 0 0 20px}
.fence-cols ul{padding:0;flex:none}
.fence-cols ul:nth-child(1){width:136px}
.fence-cols ul:nth-child(2){width:120px}
.fence-cols ul:nth-child(3){flex:1}
.fence-cols li{line-height:22.4px;white-space:nowrap}
.fence-cols .leaf{margin-top:5px}
.visit{position:absolute;left:14px;top:594px;width:442px;height:58px;background:var(--orange);color:var(--white);text-align:center;padding-top:8px}
.visit-line{font-size:17px;line-height:20px}
.visit-url{font-size:20px;letter-spacing:5px;line-height:24px}
</style>
</head>
<body>

<section class="page page--front">
  <div class="hero-photo" role="img" aria-label="Photo of a new two-storey home with a landscaped front yard"></div>
  <span class="guide guide--v1"></span>
  <span class="guide guide--v2"></span>
  <span class="guide guide--h1"></span>
  <span class="guide guide--h2"></span>
  <div class="brand-box">
    <span class="brand-mark"></span>
    <span class="brand-name">VERDANT YARDS</span>
  </div>

  <div class="offer-band">
    <h1 class="offer-title">CREATE YOUR OUTDOOR SPACE<br>WITH OUR LANDSCAPE PACKAGES</h1>
    <span class="offer-from">starting from</span>
  </div>
  <div class="price-tag">$9,990+GST</div>

  <ul class="benefits">
    <li><svg viewBox="0 0 18 16"><rect x="1" y="4" width="11" height="11" fill="none" stroke="#9cc43a" stroke-width="2"/><path d="M4 9l3 3 9-11" fill="none" stroke="#9cc43a" stroke-width="2.2"/></svg>Everything you need to love your outdoor space</li>
    <li><svg viewBox="0 0 18 16"><rect x="1" y="4" width="11" height="11" fill="none" stroke="#9cc43a" stroke-width="2"/><path d="M4 9l3 3 9-11" fill="none" stroke="#9cc43a" stroke-width="2.2"/></svg>Site consultation including a measure and quote</li>
    <li><svg viewBox="0 0 18 16"><rect x="1" y="4" width="11" height="11" fill="none" stroke="#9cc43a" stroke-width="2"/><path d="M4 9l3 3 9-11" fill="none" stroke="#9cc43a" stroke-width="2.2"/></svg>Site preparation and clearing</li>
    <li><svg viewBox="0 0 18 16"><rect x="1" y="4" width="11" height="11" fill="none" stroke="#9cc43a" stroke-width="2"/><path d="M4 9l3 3 9-11" fill="none" stroke="#9cc43a" stroke-width="2.2"/></svg>New turf including premium soil installed to front &amp; back yards</li>
    <li><svg viewBox="0 0 18 16"><rect x="1" y="4" width="11" height="11" fill="none" stroke="#9cc43a" stroke-width="2"/><path d="M4 9l3 3 9-11" fill="none" stroke="#9cc43a" stroke-width="2.2"/></svg>River rock to sides of house</li>
    <li><svg viewBox="0 0 18 16"><rect x="1" y="4" width="11" height="11" fill="none" stroke="#9cc43a" stroke-width="2"/><path d="M4 9l3 3 9-11" fill="none" stroke="#9cc43a" stroke-width="2.2"/></svg>Feature garden bed</li>
    <li><svg viewBox="0 0 18 16"><rect x="1" y="4" width="11" height="11" fill="none" stroke="#9cc43a" stroke-width="2"/><path d="M4 9l3 3 9-11" fill="none" stroke="#9cc43a" stroke-width="2.2"/></svg>Rubbish removal, clean and watering</li>
    <li><svg viewBox="0 0 18 16"><rect x="1" y="4" width="11" height="11" fill="none" stroke="#9cc43a" stroke-width="2"/><path d="M4 9l3 3 9-11" fill="none" stroke="#9cc43a" stroke-width="2.2"/></svg>Customised options available</li>
  </ul>

  <div class="call">
    <div class="call-label">CALL NOW</div>
    <div class="call-number">0400 512 377</div>
  </div>
  <div class="grass" role="img" aria-label="Illustrated strip of green grass"></div>
</section>

<section class="page page--back">
  <h2 class="intro">Create your dream lifestyle and show off<br>your personal style with our customized options!</h2>

  <div class="option opt-turf">
    <h3>Turf Options</h3>
    <ul>
      <li><span class="leaf"></span>Wintergreen</li>
      <li><span class="leaf"></span>Aussie Blue Couch</li>
      <li><span class="leaf"></span>Soft Leaf Buffalo</li>
      <li><span class="leaf"></span>Zoysia Blend</li>
      <li><span class="leaf"></span>Hybrid Bermuda</li>
    </ul>
  </div>

  <div class="option opt-rocks">
    <h3>Rocks, Pebbles &amp; Paving</h3>
    <p>Choose from our extensive options of rocks, paving, steppers</p>
  </div>

  <div class="option opt-planting">
    <h3>Planting</h3>
    <ul>
      <li><span class="leaf"></span>Custom plant selection</li>
      <li><span class="leaf"></span>Additional Garden beds</li>
    </ul>
  </div>

  <div class="option opt-other">
    <h3>Other</h3>
    <ul>
      <li><span class="leaf"></span>Mail box</li>
      <li><span class="leaf"></span>Clothesline</li>
      <li><span class="leaf"></span>Wheelie Bins Paver</li>
      <li><span class="leaf"></span>Slab</li>
      <li><span class="leaf"></span>Drainage</li>
      <li><span class="leaf"></span>Decking - Porch Entry</li>
      <li><span class="leaf"></span>Decking - Custom</li>
    </ul>
  </div>

  <div class="option opt-edging">
    <h3>Edging</h3>
    <ul>
      <li><span class="leaf"></span>Tiber Rail</li>
      <li><span class="leaf"></span>Aluminiym</li>
      <li><span class="leaf"></span>Steel</li>
      <li><span class="leaf"></span>Concrete Sleeper</li>
      <li><span class="leaf"></span>Tiber Sleeper (150mm, 200mm<br>or Stained)</li>
      <li><span class="leaf"></span>Paved edges</li>
      <li><span class="leaf"></span>Masonry</li>
      <li><span class="leaf"></span>Composite/Plastic</li>
    </ul>
  </div>

  <div class="option opt-concrete">
    <h3>Concrete</h3>
    <p>Concrete - Driveways, Paths &amp; Patios</p>
  </div>

  <div class="option opt-decking">
    <h3>Decking</h3>
  </div>

  <div class="option opt-fencing">
    <h3>Fencing</h3>
    <div class="fence-cols">
      <ul>
        <li><span class="leaf"></span>Timber Butt fence</li>
        <li><span class="leaf"></span>Glass Pool Fencing</li>
        <li><span class="leaf"></span>Good Neighbour</li>
      </ul>
      <ul>
        <li><span class="leaf"></span>Steel Sheet</li>
        <li><span class="leaf"></span>Aluminium</li>
        <li><span class="leaf"></span>Block, render etc</li>
      </ul>
      <ul>
        <li><span class="leaf"></span>Retaining Walls</li>
        <li><span class="leaf"></span>Gates &amp; Feature fencing</li>
      </ul>
    </div>
  </div>

  <div class="visit">
    <div class="visit-line">Visit our website for more ideas!</div>
    <div class="visit-url">www.verdantyards.com</div>
  </div>
</section>

</body>
</html>
```